Design Website appearance

Seeking someone to provide ideas on matters of color and contrast for the current design of the website.
Ideas top menu types and menu navigation.

https://www.filevane.net/s/8kq4pwtrm3vzx1c/Esqueleto%20de%20Interface.pdf

Target Market(s)

We sell consulting services Information Systems for medium and small businesses.

```html
<!DOCTYPE html>
<html lang="es">
<head>
<meta charset="utf-8">
<title>QBR — Quarry Bridge Systems</title>
<link href="https://fonts.googleapis.com/css2?family=Roboto+Condensed:wght@400;700&display=swap" rel="stylesheet">
<style>
:root{
  --red:#b8151b;
  --red-bright:#d41f25;
  --red-dark:#9c1014;
  --orange:#f28a1c;
  --orange-light:#fbb040;
  --yellow:#f7c51e;
  --cream:#fff8e3;
  --ink:#2b2b2b;
  --grey:#555;
  --line:#d6d6d6;
  --white:#fff;
}
*{margin:0;padding:0;box-sizing:border-box}
html,body{width:1142px;height:1200px;overflow:hidden;background:var(--white)}
body{font-family:"Roboto Condensed",Arial,sans-serif;color:var(--ink);position:relative}
a{color:inherit;text-decoration:none}
.abs{position:absolute}

/* header */
.top-links{left:745px;top:12px;display:flex;gap:14px;font-size:12px;color:var(--red)}
.brand{display:flex;align-items:center;gap:12px}
.brand-mark{width:44px;height:44px;background:var(--orange)}
.brand-name{font-size:52px;font-weight:700;color:var(--orange);line-height:1}
.brand-sub{font-size:14px;font-weight:700;color:var(--orange);letter-spacing:1px}
.header-brand{left:172px;top:44px}
.write-btn{left:558px;top:65px;width:101px;height:29px;background:linear-gradient(var(--yellow),#f0a90c);border-radius:3px;font-size:11px;font-weight:700;display:flex;align-items:center;justify-content:center;color:#222}
.divider{left:664px;top:60px;width:1px;height:62px;background:var(--line)}
.call-label{left:671px;top:64px;font-size:21px;color:var(--red)}
.phone{top:94px;display:flex;align-items:center;gap:6px;font-size:25px;font-weight:700;color:#222}
.phone-land{left:686px}
.phone-mobile{left:824px}
.header-rule{left:0;top:127px;width:1142px;height:1px;background:var(--line)}

/* nav */
.main-nav{left:0;top:128px;width:1142px;height:39px;background:linear-gradient(var(--orange-light),var(--orange));}
.main-nav ul{list-style:none;position:absolute;left:185px;top:0;height:39px;display:flex;align-items:center;gap:30px;font-size:12px;color:var(--white)}

/* hero */
.hero{left:0;top:167px;width:1142px;height:313px;background:linear-gradient(180deg,var(--cream) 0%,#fbe7a0 45%,var(--yellow) 100%)}
.hero-photo{left:480px;top:180px;width:504px;height:300px;background:radial-gradient(ellipse at 50% 45%,#e8eef4 0%,#b9c6d2 45%,rgba(247,197,30,0) 75%)}
.hero-kicker{left:199px;top:182px;font-size:25px;color:#222}
.hero-title1{left:199px;top:209px;font-size:40px;color:var(--red);line-height:1}
.hero-title2{left:199px;top:242px;font-size:64px;font-weight:700;color:var(--red);line-height:1}
.hero-copy{left:202px;top:317px;width:270px;font-size:11px;line-height:1.12;color:#222}
.start-btn{left:202px;top:424px;width:146px;height:46px;background:linear-gradient(var(--red-bright),var(--red-dark));color:var(--white);font-size:15px;font-weight:700;display:flex;align-items:center;justify-content:center;box-shadow:0 2px 3px rgba(0,0,0,.3)}

/* services band */
.services{left:0;top:480px;width:1142px;height:217px;background:linear-gradient(var(--red-bright),var(--red-dark))}
.service{position:absolute;top:12px;width:190px;height:200px;color:var(--white)}
.service h3{font-size:24px;font-weight:700;line-height:.96}
.service p{width:136px;font-size:11.5px;line-height:1.1;margin-top:12px}
.service .more{position:absolute;left:0;top:172px;font-size:15px;font-weight:700;line-height:18px}

/* consulting section */
.section-title{left:180px;top:706px;font-size:33px;font-weight:400;line-height:.92;color:var(--red)}
.section-copy{left:182px;top:778px;width:540px;font-size:11px;line-height:1.12;color:var(--grey)}
.tip{position:absolute;top:830px;width:110px}
.tip h4{font-size:11px;font-weight:700;color:var(--red);line-height:1.08}
.tip p{width:108px;font-size:11px;line-height:1.12;color:var(--grey);margin-top:16px}
.tip .more{position:absolute;top:120px;font-size:11px;font-weight:700;color:var(--red);white-space:nowrap}

.side-art1{left:742px;top:698px;width:238px;height:150px;background:linear-gradient(#f4f6f8,#c9d0d6)}
.side-art2{left:742px;top:848px;width:238px;height:75px;background:linear-gradient(var(--red-bright),var(--red-dark))}
.side-art3{left:742px;top:923px;width:238px;height:151px;background:linear-gradient(90deg,#2a2a2a,#5a5a5a 60%,#3a3a3a)}

/* footer */
.footer-rule{left:0;top:1074px;width:1142px;height:1px;background:var(--line)}
.footer-brand{left:172px;top:1094px}
.copyright{left:247px;top:1177px;font-size:11px;color:var(--red)}
.footer-nav{left:486px;top:1089px;list-style:none;font-size:11px;line-height:17px;color:var(--red)}
.social{top:1091px;width:52px;height:52px;border-radius:50%;background:#222;box-shadow:0 2px 3px rgba(0,0,0,.35)}
</style>
</head>
<body>

<header>
  <nav class="abs top-links"><a href="#">INICIO</a><a href="#">ACERCA DE NOSOTROS</a><a href="#">CONTACTENOS</a></nav>
  <div class="abs brand header-brand">
    <span class="brand-mark"></span>
    <div><div class="brand-name">QBR</div><div class="brand-sub">QUARRY BRIDGE SYSTEMS</div></div>
  </div>
  <a class="abs write-btn" href="#">ESCRIBANOS</a>
  <div class="abs divider"></div>
  <div class="abs call-label">O LLAMENOS</div>
  <div class="abs phone phone-land">
    <svg width="28" height="28" viewBox="0 0 28 28"><circle cx="14" cy="14" r="12.5" fill="none" stroke="#b8151b" stroke-width="2"/><path d="M9 8l3-1 2 4-2 1.5c.8 2 2 3.3 4 4.2l1.5-2 4 2-1 3c-6 .5-11.5-5-11.5-11.7z" fill="#b8151b"/></svg>
    6480217
  </div>
  <div class="abs phone phone-mobile">
    <svg width="16" height="28" viewBox="0 0 16 28"><rect x="1" y="1" width="14" height="26" rx="2" fill="#b8151b"/><rect x="3.5" y="4" width="9" height="8" fill="#fff"/><g fill="#fff"><rect x="3.5" y="15" width="2.5" height="2"/><rect x="7" y="15" width="2.5" height="2"/><rect x="10.5" y="15" width="2" height="2"/><rect x="3.5" y="19" width="2.5" height="2"/><rect x="7" y="19" width="2.5" height="2"/><rect x="10.5" y="19" width="2" height="2"/></g></svg>
    3120459836
  </div>
  <div class="abs header-rule"></div>
</header>

<nav class="abs main-nav">
  <ul>
    <li>ARQUITECTURA EMPRESARIA</li>
    <li>GESTION DE PROYECTOS</li>
    <li>SERVICIOS DE INFRAESTRUCTURA DE IT</li>
    <li>MIDDLEWARE</li>
    <li>APPLICACIONES</li>
    <li>BASE DE DATOS</li>
  </ul>
</nav>

<section class="abs hero"></section>
<div class="abs hero-photo" role="img" aria-label="Photo of a team of business consultants standing together"></div>
<div class="abs hero-kicker">WE HELP YOU BUILD</div>
<div class="abs hero-title1">SUCCESSFUL</div>
<div class="abs hero-title2">BUSINESS</div>
<p class="abs hero-copy">In QBR we are able to assist our clients in their needs related to a successful implementation of Orvane tools. Our experience cover the complete cycle of an implementation proyect. We have professionals (technical, functional or management). Our consultants have over 10 years of experience in the implementation of tools and Orvane solutions; extensive knowledge of business requirements of different industries.</p>
<a class="abs start-btn" href="#">START TODAY!</a>

<section class="abs services">
  <div class="service" style="left:178px"><h3>BUSINESS<br>PLAN<br>CONSULTING</h3><p>Praesent vestibulum aenean nonummy hendrerit mauris. Hasellus porta. Fusce suscipit varius mi cum sociis natoque penati-<br><br>bus et magnis dis.</p><a class="more" href="#">READ MORE..</a></div>
  <div class="service" style="left:393px"><h3>BUSINESS<br>STRATEGY<br>CONSULTING</h3><p>Praesent vestibulum aenean nonummy hendrerit mauris. Hasellus porta. Fusce suscipit varius mi cum sociis natoque penati-<br><br>bus et magnis dis.</p><a class="more" href="#">READ MORE..</a></div>
  <div class="service" style="left:599px"><h3>SALES &amp;<br>MARKETING<br>SUPPORT</h3><p>Praesent vestibulum aenean nonummy hendrerit mauris. Hasellus porta. Fusce suscipit varius mi cum sociis natoque penati-<br><br>bus et magnis dis.</p><a class="more" href="#">READ MORE..</a></div>
  <div class="service" style="left:809px"><h3>TECHNICAL &amp;<br>SUPPORT<br>CUSTOMER</h3><p>Praesent vestibulum aenean nonummy hendrerit mauris. Hasellus porta. Fusce suscipit varius mi cum sociis natoque penati-<br><br>bus et magnis dis.</p><a class="more" href="#">READ MORE..</a></div>
</section>

<h2 class="abs section-title">BEST PROFESSIONAL<br>CONSULTING AT YOUR SERVICE</h2>
<p class="abs section-copy">Praesent vestibulum aenean nonummy hendrerit mauris. Hasellus porta. Fusce suscipit varius mi cum sociis natoque pena- tibus et magnis dis parturient montes nascetur ridiculus mus. Nulla dui. Fusce feugiat malesuada odio. Morbi nunc odio</p>
<div class="tip" style="left:188px"><h4>FIND THE RIGHT<br>CONSULTANT</h4><p>Praesent vestibulum aenean non-ummy hen-drerit mauris. Hasellus porta. Fusce suscipit varius mi.</p><a class="more" href="#">READ MORE..</a></div>
<div class="tip" style="left:334px"><h4>I CAN BE YOUR<br>GUIDE IN THE WORLD<br>OF FINANCE!</h4><p style="margin-top:5px">Praesent vestibulum aenean non-ummy hen-drerit mauris. Hasellus porta. Fusce suscipit varius mi.</p><a class="more" href="#">READ MORE..</a></div>
<div class="tip" style="left:509px"><h4>SAVE TIME, SAVE<br>MONEY, GROW AND<br>SUCCEED!</h4><p style="margin-top:5px">Praesent vestibulum aenean non-ummy hen-drerit mauris. Hasellus porta. Fusce suscipit varius mi.</p><a class="more" href="#">READ MORE..</a></div>

<div class="abs side-art1" role="img" aria-label="Illustration of a large 3D version number for the Orvane database release"></div>
<div class="abs side-art2" role="img" aria-label="Banner for the Orvane database release"></div>
<div class="abs side-art3" role="img" aria-label="Photo of a person wearing Lumen Lens smart glasses"></div>

<footer>
  <div class="abs footer-rule"></div>
  <div class="abs brand footer-brand">
    <span class="brand-mark"></span>
    <div><div class="brand-name">QBR</div><div class="brand-sub">QUARRY BRIDGE SYSTEMS</div></div>
  </div>
  <div class="abs copyright">© 2013 &nbsp;|&nbsp; PRIVACY POLICY</div>
  <ul class="abs footer-nav">
    <li>ARQUITECTURA EMPRESARIA</li>
    <li>GESTION DE PROYECTOS</li>
    <li>SERVICIOS DE INFRAESTRUCTURA DE IT</li>
    <li>MIDDLEWARE</li>
    <li>APPLICACIONES</li>
    <li>BASE DE DATOS</li>
  </ul>
  <a class="abs social" style="left:710px" href="#" aria-label="Social link 1"></a>
  <a class="abs social" style="left:774px" href="#" aria-label="Social link 2"></a>
  <a class="abs social" style="left:840px" href="#" aria-label="Social link 3"></a>
  <a class="abs social" style="left:912px" href="#" aria-label="Social link 4"></a>
</footer>

</body>
</html>
```